Velmoxa AdAgency Presentation

We need ppt design for an ad agency re-branding, agency is based in Moscow, Russia. Our specifics is brand audit, consulting and strategy in web and offline.
We decided to do re-branding because our current agency does not answer the purpose and we need a kind of "second breath".
The idea of re-branding appeared because of many changes that happened in company: new clients, new projects level, new team.
So we'd like to promote company of changes and design should show this spirit as possible.
You may use info in attached pdf file (sorry for Russian language). Info is not so necessary, it will be replaced later.

Please use more colors than digital blue and grey!

Industry/Entity Type

Ad Agency

Requirements
Must have
• Logo is attached. Please choose one.

Ppt project should include:
- Front and last page design
- Heading and list design
- Page-separator design
- Diagram design
- Pics appearance

```html
<!DOCTYPE html>
<html lang="en">
<head>
<meta charset="utf-8">
<title>Velmoxa – Presentation Slides</title>
<link href="https://fonts.googleapis.com/css2?family=Roboto:wght@400;500;700&family=Roboto+Condensed:wght@700&family=Montserrat:wght@400;700&display=swap" rel="stylesheet">
<style>
  :root {
    --stage: #232323;
    --slide-bg: #e7e9ea;
    --footer-bg: #f6f6f4;
    --ink: #1e1e1e;
    --muted: #6b6b6b;
    --accent: #f2573a;
    --accent-deep: #d9432a;
    --white: #ffffff;
    --rule: #3a3a3a;
  }
  * { box-sizing: border-box; margin: 0; padding: 0; }
  html, body { width: 1200px; height: 1200px; overflow: hidden; background: var(--stage); }
  .canvas { position: relative; width: 1200px; height: 1200px; font-family: "Roboto", sans-serif; }

  .slide { position: absolute; left: 240px; width: 720px; height: 450px; overflow: hidden; }

  /* Portfolio slide */
  .slide--portfolio { top: 58px; background: radial-gradient(ellipse at 50% 40%, #f2f3f4 0%, var(--slide-bg) 70%, #dcdfe1 100%); }
  .slide__heading { position: absolute; left: 77px; top: 30px; }
  .slide__title { font-family: "Roboto Condensed", sans-serif; font-weight: 700; font-size: 16px; color: var(--ink); letter-spacing: 0.2px; }
  .slide__subtitle { font-size: 13px; color: #444; margin-top: 1px; }

  .gallery { position: absolute; left: 79px; top: 88px; width: 564px; height: 251px; display: grid; grid-template-columns: repeat(4, 1fr); grid-template-rows: repeat(2, 1fr); border: 1px solid #fff; }
  .gallery__item { width: 100%; height: 100%; }
  .gallery__item--1 { background: linear-gradient(135deg, #2e3a36, #c86a25 60%, #3b2a1c); }
  .gallery__item--2 { background: linear-gradient(160deg, #6a3a2a, #c9b7a2 50%, #4a2a22); }
  .gallery__item--3 { background: linear-gradient(135deg, #e0b560, #c98f3a 60%, #f0d28e); }
  .gallery__item--4 { background: linear-gradient(150deg, #6f8a74, #a8b8a0 55%, #3d5446); }
  .gallery__item--5 { background: linear-gradient(140deg, #6a1f12, #d0642a 55%, #3b1a10); }
  .gallery__item--6 { background: linear-gradient(150deg, #4a2a3a, #c2ac38 55%, #3a2432); }
  .gallery__item--8 { background: linear-gradient(150deg, #c9b88f, #9a8b6a 50%, #7da497); }
  .gallery__caption { background: var(--accent); color: var(--white); padding: 24px 12px 0 12px; }
  .gallery__caption-title { font-size: 10px; font-weight: 500; margin-bottom: 14px; }
  .gallery__caption-text { font-size: 7.5px; line-height: 9.5px; }

  .slide__footer { position: absolute; left: 0; bottom: 0; width: 100%; height: 54px; background: var(--footer-bg); border-bottom: 2px solid var(--accent); }
  .footer-brand { position: absolute; left: 52px; top: 8px; width: 50px; text-align: center; }
  .footer-brand__mark { display: block; width: 20px; height: 22px; margin: 0 auto 2px; background: #3c3c3c; }
  .footer-brand__name { display: block; font-size: 8px; color: #555; }
  .footer-divider { position: absolute; top: 14px; height: 26px; border-left: 1px dotted #aaa; }
  .footer-divider--left { left: 116px; }
  .footer-divider--right { left: 573px; }
  .footer-title { position: absolute; left: 146px; top: 14px; }
  .footer-title__label { font-size: 7px; color: var(--muted); }
  .footer-title__text { font-size: 13px; color: #333; margin-top: 1px; }
  .pager { position: absolute; left: 589px; top: 15px; }
  .pager__label { font-size: 5px; color: #555; letter-spacing: 0.1px; white-space: nowrap; }
  .pager__label b { color: #111; }
  .pager__controls { display: flex; align-items: center; gap: 6px; margin-top: 5px; }
  .pager__count { font-size: 9.5px; color: #333; }
  .pager__count span { color: #999; }

  /* Break slide */
  .slide--break { top: 570px; background: var(--accent); color: var(--white); }
  .break__icon { position: absolute; left: 52px; top: 186px; width: 172px; height: 172px; border-radius: 6px; background: linear-gradient(160deg, rgba(255,255,255,0.9), rgba(255,255,255,0.65)); }
  .break__text { position: absolute; left: 52px; top: 386px; }
  .break__kicker { font-family: "Montserrat", sans-serif; font-size: 12px; line-height: 12px; }
  .break__title { font-family: "Montserrat", sans-serif; font-weight: 700; font-size: 20px; line-height: 22px; margin-left: 2px; }
  .break__note { font-family: "Montserrat", sans-serif; font-size: 7.5px; margin-left: 2px; margin-top: 1px; }

  /* Showcase footer */
  .showcase-rule { position: absolute; left: 38px; top: 1067px; width: 1108px; border-top: 1px solid var(--rule); }
  .showcase-brand { position: absolute; left: 96px; top: 1084px; width: 100px; text-align: center; }
  .showcase-brand__mark { display: block; width: 52px; height: 58px; margin: 0 auto 12px; background: #e8e8e8; }
  .showcase-brand__name { display: block; font-size: 21px; color: #e8e8e8; }
  .showcase-caption { position: absolute; left: 728px; top: 1112px; font-size: 19px; color: var(--white); letter-spacing: 0.2px; white-space: nowrap; }
</style>
</head>
<body>
<div class="canvas">

  <section class="slide slide--portfolio">
    <header class="slide__heading">
      <h1 class="slide__title">OUR PORTFOLIO</h1>
      <p class="slide__subtitle">How to images displayed</p>
    </header>

    <div class="gallery">
      <div class="gallery__item gallery__item--1" role="img" aria-label="Portfolio artwork: colourful illustrated elephant"></div>
      <div class="gallery__item gallery__item--2" role="img" aria-label="Portfolio artwork: illustrated monster character"></div>
      <div class="gallery__item gallery__item--3" role="img" aria-label="Portfolio artwork: illustrated characters in golden tones"></div>
      <div class="gallery__item gallery__item--4" role="img" aria-label="Portfolio artwork: green toned character illustration"></div>
      <div class="gallery__item gallery__item--5" role="img" aria-label="Portfolio artwork: orange owl illustration"></div>
      <div class="gallery__item gallery__item--6" role="img" aria-label="Portfolio artwork: yellow creature illustration"></div>
      <div class="gallery__item gallery__caption">
        <p class="gallery__caption-title">Title Image</p>
        <p class="gallery__caption-text">This section can be pop up effect.<br>All of content/description<br>write here</p>
      </div>
      <div class="gallery__item gallery__item--8" role="img" aria-label="Portfolio artwork: character sitting on clouds"></div>
    </div>

    <footer class="slide__footer">
      <div class="footer-brand">
        <span class="footer-brand__mark"></span>
        <span class="footer-brand__name">Velmoxa</span>
      </div>
      <div class="footer-divider footer-divider--left"></div>
      <div class="footer-title">
        <p class="footer-title__label">Slide title</p>
        <p class="footer-title__text">Our Portfolio</p>
      </div>
      <div class="footer-divider footer-divider--right"></div>
      <div class="pager">
        <p class="pager__label">WE ARE CURRETLY <b>HERE</b></p>
        <div class="pager__controls">
          <svg width="16" height="16" viewBox="0 0 16 16" aria-label="Previous slide"><circle cx="8" cy="8" r="8" fill="#f2573a"/><path d="M9.5 4.5 6 8l3.5 3.5" fill="none" stroke="#fff" stroke-width="1"/></svg>
          <span class="pager__count">5 <span>Of 8</span></span>
          <svg width="16" height="16" viewBox="0 0 16 16" aria-label="Next slide"><circle cx="8" cy="8" r="8" fill="#f2573a"/><path d="M6.5 4.5 10 8l-3.5 3.5" fill="none" stroke="#fff" stroke-width="1"/></svg>
        </div>
      </div>
    </footer>
  </section>

  <section class="slide slide--break">
    <div class="break__icon" role="img" aria-label="Illustration of a steaming coffee cup"></div>
    <div class="break__text">
      <p class="break__kicker">NEXT</p>
      <h2 class="break__title">GRAB A COFFEE</h2>
      <p class="break__note">Back again in 15 minutes...Thanks for your patience</p>
    </div>
  </section>

  <div class="showcase-rule"></div>
  <div class="showcase-brand">
    <span class="showcase-brand__mark"></span>
    <span class="showcase-brand__name">Velmoxa</span>
  </div>
  <p class="showcase-caption">POWER POINT PRESENTATION</p>

</div>
</body>
</html>
```